Carpentry and Building Business Card

I'm looking for a business card that is minimalistic and that incorporates the theme of my Velmor logo.
On one side I'd like the VELMOR logo with my details on the other side.
Double sided with curved edges

Target Market(s)

Construction / renovation
Adults

Industry/Entity Type

Tradesman

Contact Information for Business Card

Logo on one side, details on the other

Colors

Designer to choose only greyscale colors for use in the design.

Requirements
Must have
• Nilo Petrakis
VELMOR CONSTRUCT
Carpentry & Building Services
0481236574
Velmorconstruct@brixmail.com
Lic No. 718263D
Nice to have
• Fb and insta icons. @velmorconstruct
Should not have
• No hammer or tool icons please.

No address line.

```html
<!DOCTYPE html>
<html lang="en">
<head>
<meta charset="utf-8">
<title>Velmor Construct – Business Card</title>
<link href="https://fonts.googleapis.com/css2?family=Montserrat:wght@400;500;600&family=Arimo:wght@400&display=swap" rel="stylesheet">
<style>
  :root {
    --stage: #3b3b3c;
    --card: #1f1c1d;
    --accent: #ea8a2e;
    --ink: #f2f2f2;
    --ink-soft: #d9d9d9;
  }
  * { margin: 0; padding: 0; box-sizing: border-box; }
  html, body {
    width: 1200px; height: 800px; overflow: hidden;
    background: var(--stage);
  }
  .canvas {
    position: relative; width: 1200px; height: 800px;
    display: flex; align-items: center; justify-content: center; gap: 50px;
  }
  .card {
    position: relative;
    width: 530px; height: 310px;
    background: var(--card);
    border-radius: 22px;
    box-shadow: 0 3px 0 var(--accent);
  }

  /* Details side */
  .details-mark {
    position: absolute; top: 36px; right: 44px;
    display: flex; align-items: center; gap: 8px;
    font-family: "Montserrat", sans-serif; font-weight: 500;
    font-size: 13px; letter-spacing: 0.3em; color: var(--accent);
  }
  .mark-square {
    width: 14px; height: 14px; border: 2px solid var(--accent);
  }
  .person {
    position: absolute; left: 44px; bottom: 42px;
  }
  .person-name {
    font-family: "Montserrat", sans-serif; font-weight: 600;
    font-size: 19px; letter-spacing: 0.22em; color: var(--accent);
    text-transform: uppercase;
  }
  .name-rule {
    width: 30px; height: 2px; background: var(--accent);
    margin: 12px 0 12px;
  }
  .contact-list { list-style: none; }
  .contact-item {
    display: flex; align-items: center; gap: 9px;
    font-family: "Arimo", sans-serif; font-size: 13px;
    color: var(--ink-soft); line-height: 19px;
  }
  .contact-icon { width: 11px; height: 11px; flex: none; }
  .licence { padding-left: 20px; }

  /* Brand side */
  .brand {
    position: absolute; left: 0; right: 0; top: 100px;
    display: flex; align-items: center; justify-content: center; gap: 22px;
  }
  .brand-square {
    width: 60px; height: 60px; border: 3px solid var(--accent);
  }
  .brand-name {
    font-family: "Montserrat", sans-serif; font-weight: 600;
    font-size: 46px; letter-spacing: 0.32em; color: var(--ink);
    margin-right: -0.32em;
  }
  .tagline {
    position: absolute; left: 0; right: 0; top: 205px; text-align: center;
    font-family: "Montserrat", sans-serif; font-weight: 500;
    font-size: 12px; letter-spacing: 0.3em; color: var(--ink);
  }
  .tagline .amp { color: var(--accent); }
</style>
</head>
<body>
<main class="canvas">
  <section class="card card-details" aria-label="Contact details side">
    <div class="details-mark"><span class="mark-square"></span>VELMOR</div>
    <div class="person">
      <h1 class="person-name">Nilo Petrakis</h1>
      <div class="name-rule"></div>
      <ul class="contact-list">
        <li class="contact-item">
          <svg class="contact-icon" viewBox="0 0 12 12"><path d="M3 1 L5 3.5 L4 5 Q5 7 7 8 L8.5 7 L11 9 L10 11 Q5 11 1 3 Z" fill="var(--accent)"/></svg>
          048-123-6574
        </li>
        <li class="contact-item">
          <svg class="contact-icon" viewBox="0 0 12 12"><rect x="0.5" y="2" width="11" height="8" fill="var(--accent)"/><path d="M0.5 2 L6 7 L11.5 2" stroke="var(--card)" stroke-width="1.2" fill="none"/></svg>
          Velmorconstruct@brixmail.com
        </li>
        <li class="contact-item">
          <svg class="contact-icon" viewBox="0 0 12 12"><circle cx="6" cy="6" r="5.5" fill="var(--accent)"/></svg>
          velmorconstruct
        </li>
        <li class="contact-item">
          <svg class="contact-icon" viewBox="0 0 12 12"><circle cx="6" cy="6" r="5.5" fill="var(--accent)"/></svg>
          @velmorconstruct
        </li>
        <li class="contact-item licence">LIC NO: 718263D</li>
      </ul>
    </div>
  </section>

  <section class="card card-brand" aria-label="Brand side">
    <div class="brand">
      <span class="brand-square"></span>
      <span class="brand-name">VELMOR</span>
    </div>
    <p class="tagline">CARPENTRY <span class="amp">&amp;</span> BUILDING SERVICES</p>
  </section>
</main>
</body>
</html>
```